We need a flyer design for a new fencing business. We do ferrowane fencing instalations and pride our company on Reliabilty, Dependabilty and genuine quality. Because it's not just a fence... It's your fence. Our company offers customer free quotes. Things that would need to be on the flyer;

*Company Name - Valley Copperpath Fencing
*Company email - copperpathfencing@quillmail.net
*Company Phone number - 0455 912 307

*Ferrowane fence specialist
*Free quotes

```html
<!DOCTYPE html>
<html lang="en">
<head>
<meta charset="UTF-8">
<title>Valley Copperpath Fencing – Flyer</title>
<link rel="stylesheet" href="https://fonts.googleapis.com/css2?family=Cinzel:wght@400;700&family=Oswald:wght@400;600&family=Bubblegum+Sans&display=swap">
<style>
  :root {
    --paper: #ffffff;
    --orange: #e2661f;
    --orange-light: #f08a3a;
    --orange-deep: #b8440f;
    --ink: #2a1a12;
    --band: #2b1b14;
    --cream: #f6e7d6;
    --yellow: #ffe23a;
    --splat: #5b2430;
    --fence-dark: #9a3a0c;
    --fence-light: #e9844a;
  }
  * { box-sizing: border-box; margin: 0; padding: 0; }
  html, body { width: 900px; height: 1200px; overflow: hidden; background: var(--paper); }
  .flyer {
    position: relative; width: 900px; height: 1200px;
    background: var(--paper); overflow: hidden;
    font-family: 'Cinzel', serif;
  }
  .flyer-header {
    position: absolute; left: 0; top: 0; width: 900px; height: 240px;
    display: flex; align-items: center; padding: 0 48px;
  }
  .brand {
    display: flex; align-items: center; gap: 12px; width: 250px;
  }
  .brand-square { width: 22px; height: 22px; background: var(--orange); flex: none; }
  .brand-name {
    font-family: 'Cinzel', serif; font-weight: 700; font-size: 22px;
    line-height: 1.15; color: var(--orange); text-transform: uppercase;
  }
  .specialist { flex: 1; text-align: center; }
  .specialist-product {
    font-size: 56px; font-weight: 700; color: var(--orange); letter-spacing: 2px;
    padding-bottom: 10px; border-bottom: 3px solid var(--ink);
  }
  .specialist-role {
    font-size: 46px; color: var(--ink); letter-spacing: 2px; padding-top: 10px;
  }
  .flyer-body {
    position: absolute; left: 0; top: 240px; width: 900px; height: 960px;
    background: radial-gradient(ellipse at 50% 30%, var(--orange-light) 0%, var(--orange) 45%, var(--orange-deep) 100%);
  }
  .company-name { text-align: center; color: var(--paper); padding-top: 40px; }
  .company-name .first {
    display: block; font-size: 176px; line-height: 1; letter-spacing: 6px;
    font-weight: 400;
  }
  .company-name .rest {
    display: block; font-size: 62px; letter-spacing: 2px; margin-top: 14px;
  }
  .values-band {
    position: absolute; left: 0; top: 380px; width: 900px; height: 74px;
    background: var(--band); color: var(--cream);
    display: flex; align-items: center; justify-content: center; gap: 22px;
    font-family: 'Oswald', sans-serif; font-size: 30px; letter-spacing: 2px;
    text-transform: uppercase;
  }
  .free-quotes {
    position: absolute; left: 60px; top: 490px; width: 240px; height: 240px;
    border-radius: 50%; background: var(--splat);
    display: flex; align-items: center; justify-content: center; text-align: center;
    font-family: 'Bubblegum Sans', sans-serif; font-size: 50px; line-height: 1;
    color: var(--paper); transform: rotate(-8deg); z-index: 2;
  }
  .tagline {
    position: absolute; left: 350px; top: 490px; width: 510px;
    font-family: 'Bubblegum Sans', sans-serif; color: var(--yellow);
    font-size: 44px; line-height: 1.15; z-index: 2;
  }
  .tagline .first { display: block; }
  .tagline .second { display: block; text-align: right; }
  .call-to-action {
    position: absolute; left: 440px; top: 610px; color: var(--yellow);
    font-family: 'Oswald', sans-serif; z-index: 2;
  }
  .call-now { font-size: 56px; font-weight: 600; line-height: 1; }
  .call-sub { font-size: 30px; line-height: 1.1; }
  .call-phone { font-size: 54px; font-weight: 600; line-height: 1.1; letter-spacing: 1px; }
  .fence-art {
    position: absolute; left: 0; bottom: 0; width: 900px; height: 160px;
    background: linear-gradient(to top, var(--fence-dark) 0%, var(--fence-dark) 35%, var(--fence-light) 100%);
    opacity: 0.9; z-index: 1;
  }
  .email-line {
    position: absolute; left: 0; bottom: 22px; width: 900px; text-align: center;
    font-family: 'Oswald', sans-serif; font-size: 22px; color: var(--cream);
    letter-spacing: 0.5px; z-index: 2;
  }
</style>
</head>
<body>
<main class="flyer">
  <header class="flyer-header">
    <div class="brand">
      <span class="brand-square"></span>
      <span class="brand-name">Valley Copperpath Fencing</span>
    </div>
    <div class="specialist">
      <div class="specialist-product">FERROWANE</div>
      <div class="specialist-role">FENCE SPECIALIST</div>
    </div>
  </header>

  <section class="flyer-body">
    <h1 class="company-name">
      <span class="first">VALLEY</span>
      <span class="rest">COPPERPATH FENCING</span>
    </h1>

    <div class="values-band">
      <span>Reliability</span><span>•</span>
      <span>Dependability</span><span>•</span>
      <span>Genuine Quality</span>
    </div>

    <div class="free-quotes">FREE<br>QUOTES!</div>

    <p class="tagline">
      <span class="first">"It's not just a fence...</span>
      <span class="second">It's YOUR fence"</span>
    </p>

    <div class="call-to-action">
      <div class="call-now">CALL NOW</div>
      <div class="call-sub">for a free quote</div>
      <div class="call-phone">0455 912 307</div>
    </div>

    <div class="fence-art" role="img" aria-label="Silhouette of a picket fence and tall grass along the bottom edge"></div>
    <p class="email-line">Or email us at copperpathfencing@quillmail.net</p>
  </section>
</main>
</body>
</html>
```